Book Cover (HALF OF ALL WORRIES FADE AWAY)

This book is a series of blog posts from my blog, Notes Fit for Borrowing, which is at glenmarwick.com/blog.
The book is to be called:
HALF OF ALL WORRIES FADE AWAY
And 51 other Notes Fit for Borrowing from the Small Business Sage
(Notes Fit for Borrowing) should be italicized.
My name is Glen Marwick, M.B.A.

I will need three variations for my paperback, hardcover and e-book.
Here are some of the blog titles and their topics:
Preparing Your Small Business For Recession small business recession
Should I Incorporate My Business? Should I Incorporate My Business?
Alternative to Minority Shareholder In Small Private Companies minority shareholder
Small Business Culture – Getting it Right Small Business Culture
What is The Right Way to Fire Someone The Right Way to Fire Someone
The Five Basic Leadership Principles Leadership Principles
10 Tips for New Entrepreneurs – Sure Ways to Increase Your Chances of Success
10 things to consider before becoming an entrepreneur
Strategy vs Biz Plans small business strategy
Closing Sales close the sale
Breakeven break even
Growth makes cash flow suck cash flow issues
Think Twice About Offering Early Payment Discounts prepayment discounts
Firing Customers firing customers
Collections best practices getting paid faster
The Cash Flow Statement cash flow statement
Using Paralegals paralegal
Radical Candor radical candor
Why No is the Second Best Word to a Salesperson's ears value of no
The $8 Million Problem -
Contractor vs Employee contractor vs employee
The Vantrell sales tactic
Systems Turn Goals From Dreams Into Reality Systems vs Goals
The Importance of Realistic Goals stretch goals
Why The Owner Must Review Every Hire hiring for values
Systems Thinking for Small Biz: The Case for SOPs systems thinking
Trust Your Gut business intuition
Grease and friction grease vs friction
Left alone, 90% of problems solve themselves strategic inaction
Referrals Are Great—But Not a Growth Strategy referrals
The Lean Marketing Machine: 7 Hacks to Grow Your Small Business Fast marketing hacks
The Small Business Health Check small business health check
How to Spot a Customer Headed for Trouble — Before They Take You Down With Them customer warning signs
We Are What We Repeatedly Do habits
The Smartest People Know When to Play Dumb playing dumb
Before You Scale, Do the Math unit economics
AI for Small Business: Practical Tools and Use Cases AI for Small Business
Title: Tell Me Right Now—Why Can’t We Raise Your Prices? small business pricing
Why Your Real Competitor Isn’t Who You Think creative destruction
Good Enough Might Be Great satisficing
Bootstrapping: Building Your Business on Your Terms bootstrapping
Building Resilient Companies That Never Have to Bet the Farm bet the farm
We Always Overshoot: From Fiber to Cannabis to AI AI overbuild
A Bias Toward Action bias toward ation
Choosing the Right Business Owner Title business owner title
Jobs to Be Done: Understanding What Your Customers Really Want Jobs to Be Done
Forget Money. Here’s What Really Motivates People. motivation

Target Market(s)

Small business operators, business school students

Industry/Entity Type

Small business

Colors

Designer to choose colors to be used in the design.

Requirements
Should not have
• Should not look cartoonish

```html
<!DOCTYPE html>
<html lang="en">
<head>
<meta charset="utf-8">
<title>Half of All Worries Fade Away — Book Cover</title>
<link href="https://fonts.googleapis.com/css2?family=Bebas+Neue&family=Alegreya:ital,wght@1,400;1,700&family=Oswald:wght@600&display=swap" rel="stylesheet">
<style>
  :root {
    --night: #111d35;
    --deep-blue: #17335a;
    --dusk-grey: #4b4a55;
    --dusk-brown: #7a5f45;
    --sunset-orange: #e49e42;
    --sunset-gold: #efbe56;
    --ink-white: #ffffff;
    --soft-white: #f4f1ea;
    --accent-gold: #f1d9a0;
  }
  html, body {
    margin: 0;
    padding: 0;
    width: 873px;
    height: 1200px;
    overflow: hidden;
    background: var(--night);
  }
  .cover {
    position: relative;
    width: 873px;
    height: 1200px;
    overflow: hidden;
    background: linear-gradient(to bottom,
      var(--night) 0%,
      var(--night) 18%,
      var(--deep-blue) 45%,
      var(--dusk-grey) 60%,
      var(--dusk-brown) 70%,
      var(--sunset-orange) 84%,
      var(--sunset-gold) 95%,
      var(--sunset-gold) 100%);
  }
  .cover-art {
    position: absolute;
    inset: 0;
  }
  .title {
    position: absolute;
    left: 0;
    right: 0;
    top: 218px;
    margin: 0;
    padding-left: 18px;
    text-align: center;
    font-family: "Bebas Neue", "Arial Narrow", sans-serif;
    font-weight: 400;
    color: var(--ink-white);
    font-size: 100px;
    line-height: 90px;
    letter-spacing: 1px;
  }
  .title span { display: block; }
  .subtitle {
    position: absolute;
    left: 0;
    right: 0;
    top: 822px;
    margin: 0;
    text-align: center;
    font-family: "Alegreya", Georgia, serif;
    font-style: italic;
    font-weight: 400;
    font-size: 35px;
    line-height: 43px;
    color: var(--soft-white);
    letter-spacing: 0.5px;
  }
  .subtitle .count {
    color: var(--accent-gold);
    font-weight: 700;
    font-variant-numeric: oldstyle-nums;
  }
  .author {
    position: absolute;
    left: 0;
    right: 0;
    top: 1080px;
    margin: 0;
    text-align: center;
    font-family: "Oswald", "Arial Narrow", sans-serif;
    font-weight: 600;
    font-size: 38px;
    letter-spacing: 7px;
    color: var(--ink-white);
  }
</style>
</head>
<body>
  <main class="cover">
    <svg class="cover-art" width="873" height="1200" viewBox="0 0 873 1200" aria-hidden="false">
      <defs>
        <filter id="cloud-glow" x="-10%" y="-10%" width="120%" height="120%">
          <feGaussianBlur stdDeviation="2" result="blur"/>
          <feMerge><feMergeNode in="blur"/><feMergeNode in="SourceGraphic"/></feMerge>
        </filter>
        <radialGradient id="flare-core" cx="50%" cy="50%" r="50%">
          <stop offset="0%" stop-color="#ffffff" stop-opacity="1"/>
          <stop offset="100%" stop-color="#ffffff" stop-opacity="0"/>
        </radialGradient>
        <linearGradient id="flare-h" x1="0" x2="1" y1="0" y2="0">
          <stop offset="0%" stop-color="#fff" stop-opacity="0"/>
          <stop offset="50%" stop-color="#fff" stop-opacity="0.9"/>
          <stop offset="100%" stop-color="#fff" stop-opacity="0"/>
        </linearGradient>
        <linearGradient id="flare-v" x1="0" x2="0" y1="0" y2="1">
          <stop offset="0%" stop-color="#fff" stop-opacity="0"/>
          <stop offset="50%" stop-color="#fff" stop-opacity="0.9"/>
          <stop offset="100%" stop-color="#fff" stop-opacity="0"/>
        </linearGradient>
      </defs>

      <g class="thought-cloud" fill="none" stroke="var(--soft-white)" stroke-width="3.5" filter="url(#cloud-glow)">
        <path d="M 175,300
                 C 150,230 230,195 285,228
                 C 320,150 470,140 502,198
                 C 560,165 622,182 628,232
                 C 700,222 742,272 700,335
                 C 800,355 835,465 745,508
                 C 760,600 662,640 602,602
                 C 560,640 455,642 408,605
                 C 400,632 362,640 345,612
                 C 310,620 290,600 288,578
                 C 225,600 172,565 196,525
                 C 118,545 82,440 150,412
                 C 128,380 140,320 175,300 Z"/>
        <circle cx="287" cy="691" r="21"/>
        <circle cx="270" cy="745" r="15"/>
        <circle cx="259" cy="791" r="11"/>
        <circle cx="263" cy="830" r="7"/>
      </g>

      <g class="lens-flare">
        <rect x="600" y="228" width="240" height="2" fill="url(#flare-h)"/>
        <rect x="717" y="150" width="2" height="170" fill="url(#flare-v)"/>
        <circle cx="718" cy="229" r="14" fill="url(#flare-core)"/>
      </g>

      <g class="gear-illustrations" fill="#ffffff" fill-opacity="0.05">
        <circle cx="228" cy="284" r="50" role="img" aria-label="Outline gear illustration"/>
        <rect x="620" y="250" width="125" height="92" rx="40" role="img" aria-label="Pair of outline gear illustrations"/>
        <rect x="278" y="490" width="430" height="128" rx="60" role="img" aria-label="Row of interlocking outline gear illustrations"/>
      </g>
    </svg>

    <h1 class="title">
      <span>HALF OF</span>
      <span>ALL WORRIES</span>
      <span>FADE AWAY</span>
    </h1>

    <p class="subtitle">
      And <span class="count">51</span> other Notes<br>
      Fit for Borrowing from the<br>
      Small Business Sage
    </p>

    <p class="author">GLEN MARWICK, M.B.A</p>
  </main>
</body>
</html>
```